Website for Brisbeck Current Glide

Require a website for a river float in the City of Edmonton. Located on North Saskatchewan River. Will need to be a coded website with incorporated booking system through Fare Harbor software.

Pages include
Home
Pricing
About
FAQ
Contact

Brisbeck Current Glide is an activity based business that will have customers floating down the North Saskatchewan river in Edmonton AB. The site will have all information needed and a full reservation system. The project was launched to provide people in the Edmonton area a favorite summer activity.

Here are similar websites to reference what our business will be doing and what we are looking for.

mellowbendcanoehire.example
pinegulchloopers.example

Target Market(s)

Families, Groups, Individuals, Anyone who wants to explore the river

Industry/Entity Type

Activities based business/ Outdoor recreational/ River Float

Coding

Coded - Design and coding required

Number of Pages Required

5+ page

Colors
0054AA
0677BA
7BADD7
CADEEF
E8F1F8
F0912C
F2A743
F7CA91
FBE8D2
FDF5EE

```html
<!DOCTYPE html>
<html lang="en">
<head>
<meta charset="utf-8">
<title>Brisbeck Current Glide</title>
<link href="https://fonts.googleapis.com/css2?family=Montserrat:wght@400;500;600;700;800&display=swap" rel="stylesheet">
<style>
:root{
  --navy:#0b2d5e;
  --blue:#0054AA;
  --mid-blue:#0677BA;
  --sky:#7BADD7;
  --band:#a6dcef;
  --faq:#52c4e7;
  --faq-dark:#27729a;
  --card:#1f88f2;
  --pale:#E8F1F8;
  --orange:#F0912C;
  --orange-soft:#F2A743;
  --peach:#FBE8D2;
  --cream:#FDF5EE;
  --ink:#1d2733;
  --text:#4a4f57;
  --white:#ffffff;
}
*{box-sizing:border-box;margin:0;padding:0}
html,body{width:1200px;height:3831px;overflow:hidden}
body{position:relative;font-family:'Montserrat',sans-serif;background:var(--white);color:var(--ink)}
.abs{position:absolute}
.btn{position:absolute;display:flex;align-items:center;justify-content:center;gap:8px;border-radius:20px;font-weight:700;font-size:15px;letter-spacing:1.5px;text-transform:uppercase;color:var(--white)}
.btn .dot{width:17px;height:17px;border-radius:50%;background:var(--white);display:flex;align-items:center;justify-content:center}
.btn .dot svg{width:9px;height:9px}
.btn-orange{background:var(--orange)}
.btn-navy{background:var(--navy)}
.btn-sky{background:var(--faq)}

/* header */
.site-header{position:absolute;left:0;top:0;width:1200px;height:118px;background:var(--white)}
.nav-link{position:absolute;top:53px;font-size:15px;font-weight:500;letter-spacing:2.4px;color:var(--ink)}
.nav-link.active{color:var(--orange)}
.brand{position:absolute;left:520px;top:30px;width:160px;text-align:center}
.brand-mark{width:40px;height:40px;border-radius:50%;background:var(--mid-blue);margin:0 auto 6px}
.brand-name{font-size:13px;font-weight:800;color:var(--navy);letter-spacing:.5px;line-height:1.1}

/* hero */
.hero-photo{position:absolute;left:0;top:118px;width:1200px;height:500px;background:linear-gradient(180deg,#8c8fcf 0%,#6c6fb4 40%,#4e6aa0 70%,#3e6a72 100%)}
.hero-title{position:absolute;left:0;top:224px;width:1200px;text-align:center;color:var(--white);font-weight:800;font-size:72px;line-height:74px;letter-spacing:1px}
.hero-sub{position:absolute;left:0;top:394px;width:1200px;text-align:center;color:var(--white);font-size:15px;font-weight:500}
.hero-dots{position:absolute;left:1044px;top:308px}
.hero-dots span{display:block;width:8px;height:8px;border-radius:50%;background:#fff;opacity:.8;margin-bottom:14px}

/* pricing band */
.price-label{position:absolute;left:156px;top:667px;font-size:44px;font-weight:800;color:var(--navy);letter-spacing:1px}
.price-item{position:absolute;left:434px;top:648px;font-size:36px;font-weight:400;color:var(--navy)}
.price-amount{position:absolute;left:434px;top:690px;font-size:35px;font-weight:700;color:var(--orange)}

/* includes */
.includes-head{position:absolute;left:159px;top:897px;font-size:16px;font-weight:700;letter-spacing:2px;line-height:19px;color:var(--ink)}
.includes-tube{position:absolute;left:159px;top:953px;font-size:16px;font-weight:700;line-height:19px;color:var(--ink)}
.feature{position:absolute;width:190px;text-align:center;font-size:16px;font-weight:700;letter-spacing:2px;line-height:19px}
.feature-icon{position:relative;width:80px;height:66px;margin:0 auto 8px}
.feature-icon .bubble{position:absolute;right:0;top:2px;width:50px;height:50px;border-radius:50%;background:var(--pale)}
.feature-icon .glyph{position:absolute;left:12px;top:6px;width:46px;height:54px;border:3px solid var(--orange);border-radius:10px}
.includes-photo{position:absolute;left:686px;top:898px;width:357px;height:361px;border-radius:4px;background:linear-gradient(160deg,#7a8a5e 0%,#5e6c48 40%,#d9374f 70%,#8a5a3a 100%)}

/* group band */
.group-band{position:absolute;left:0;top:1359px;width:1200px;height:163px;background:linear-gradient(90deg,#2a6f93 0%,#3c8db0 50%,#2b6f8f 100%)}
.group-title{position:absolute;left:158px;top:1414px;font-size:34px;font-weight:800;color:var(--white);letter-spacing:.5px}
.group-note{position:absolute;left:158px;top:1457px;font-size:12px;color:#dfe9ef}

/* about */
.about-bg{position:absolute;left:0;top:1522px;width:1200px;height:598px;background:linear-gradient(180deg,#fff 0%,#f5f9fc 100%)}
.about-photo{position:absolute;left:88px;top:1640px;width:460px;height:360px;border-radius:230px 230px 120px 200px;background:linear-gradient(150deg,#5fc7d6 0%,#2c9fb8 50%,#f0b1a5 100%)}
.about-title{position:absolute;left:599px;top:1616px;font-size:48px;font-weight:800;color:var(--navy)}
.about-lead{position:absolute;left:600px;top:1682px;width:420px;font-size:16px;line-height:23px;color:var(--faq)}
.about-copy{position:absolute;left:600px;width:440px;font-size:13px;line-height:22px;color:var(--text)}
.about-copy a{color:var(--orange);text-decoration:none}

/* faq */
.faq-band{position:absolute;left:0;top:2119px;width:1200px;height:569px;background:var(--faq)}
.faq-title{position:absolute;left:0;top:2188px;width:1200px;text-align:center;font-size:46px;font-weight:700;color:var(--white)}
.faq-item{position:absolute;width:420px;height:53px;border:1.5px solid var(--white);display:flex;align-items:center}
.faq-item .toggle{width:45px;height:100%;background:var(--orange);display:flex;align-items:center;justify-content:center}
.faq-item .q{margin-left:20px;font-size:16px;color:var(--white)}
.faq-item.open{background:var(--faq-dark)}
.faq-answer{position:absolute;left:174px;top:2390px;width:420px;height:131px;background:var(--faq-dark);border:1.5px solid var(--white);border-top:none;padding:18px 14px;color:var(--white);font-size:13px;line-height:19px}
.faq-answer u{display:block;margin-top:12px;font-size:12px;font-weight:600}

/* contact */
.map{position:absolute;left:158px;top:2805px;width:884px;height:431px;border-radius:4px;background:linear-gradient(135deg,#e6e6e6 0%,#d8d8d8 100%)}
.contact-card{position:absolute;left:219px;top:2871px;width:383px;height:335px;background:var(--card);padding:46px 52px;color:var(--white)}
.contact-card h2{font-size:28px;font-weight:700;letter-spacing:.5px}
.contact-card .tag{font-size:16px;font-weight:600;margin-top:4px}
.contact-line{display:flex;align-items:center;gap:8px;font-size:16px;margin-top:10px}
.contact-line:first-of-type{margin-top:26px}
.ring{width:20px;height:20px;border-radius:50%;border:1.5px solid var(--white);display:flex;align-items:center;justify-content:center}
.ring svg{width:10px;height:10px}
.socials{display:flex;gap:14px;margin-top:20px}
.socials span{width:24px;height:24px;border-radius:50%;border:1.5px solid currentColor}
.contact-card .visit{font-size:13px;line-height:19px;margin-top:18px}

/* footer */
.footer-col-title{position:absolute;font-size:24px;font-weight:500;color:var(--white)}
.footer-link{position:absolute;left:526px;font-size:16px;font-weight:500;letter-spacing:2.5px;color:var(--white)}
.footer-brand{position:absolute;left:200px;top:3480px;width:200px;text-align:center}
.footer-brand .brand-mark{width:70px;height:70px;background:var(--faq);margin-bottom:12px}
.footer-brand .brand-name{color:var(--white);font-size:20px}
.copyright{position:absolute;left:0;top:3772px;width:1200px;text-align:center;font-size:10px;color:#c5d3e6}
</style>
</head>
<body>

<header class="site-header">
  <span class="nav-link active" style="left:202px">HOME</span>
  <span class="nav-link" style="left:297px">PRICING</span>
  <span class="nav-link" style="left:414px">ABOUT</span>
  <div class="brand"><div class="brand-mark"></div><div class="brand-name">Brisbeck Current Glide</div></div>
  <span class="nav-link" style="left:718px">FAQ</span>
  <span class="nav-link" style="left:795px">CONTACT</span>
  <div class="btn btn-orange" style="left:923px;top:43px;width:166px;height:38px">Book Now<span class="dot"><svg viewBox="0 0 10 10"><path d="M3 1l4 4-4 4" fill="none" stroke="#F0912C" stroke-width="2"/></svg></span></div>
</header>

<section class="hero">
  <div class="hero-photo" role="img" aria-label="Downtown Edmonton skyline and bridge over the North Saskatchewan River at dusk"></div>
  <h1 class="hero-title">BRISBECK<br>CURRENT GLIDE</h1>
  <p class="hero-sub">Float the North Saskatchewan through downtown Edmonton</p>
  <div class="btn btn-orange" style="left:496px;top:453px;width:165px;height:37px">Book Now<span class="dot"><svg viewBox="0 0 10 10"><path d="M3 1l4 4-4 4" fill="none" stroke="#F0912C" stroke-width="2"/></svg></span></div>
  <div class="hero-dots"><span></span><span></span><span></span></div>
</section>

<svg class="abs" style="left:0;top:560px" width="1200" height="270" viewBox="0 0 1200 270">
  <path d="M0 18 C60 -5 110 30 170 20 C240 5 300 30 380 22 C450 12 520 35 600 25 C700 10 800 38 900 30 C980 22 1050 2 1120 10 C1160 15 1185 5 1200 4 L1200 222 C1150 210 1110 200 1060 215 C1000 232 950 210 880 222 C820 232 760 222 700 230 C640 238 600 222 540 228 C470 236 430 262 380 255 C330 248 300 232 250 238 C190 245 150 225 90 228 C50 230 20 222 0 218 Z" fill="var(--band)"/>
</svg>

<section class="pricing">
  <h2 class="price-label">PRICING</h2>
  <p class="price-item">Tube and Shuttle</p>
  <p class="price-amount">$30/person</p>
  <div class="btn btn-navy" style="left:843px;top:677px;width:165px;height:37px">Book Now<span class="dot"><svg viewBox="0 0 10 10"><path d="M3 1l4 4-4 4" fill="none" stroke="#0b2d5e" stroke-width="2"/></svg></span></div>
</section>

<section class="includes">
  <p class="includes-head">WE KEEP OUR PRICING SIMPLE AND INCLUDE<br>EVERYTHING YOU NEED:</p>
  <p class="includes-tube">Premium comfort float tube with backrest<br>and cup holder</p>

  <div class="feature" style="left:120px;top:1020px"><div class="feature-icon" role="img" aria-label="Lifejacket icon"><span class="bubble"></span><span class="glyph"></span></div>LIFEJACKET</div>
  <div class="feature" style="left:275px;top:1020px"><div class="feature-icon" role="img" aria-label="Paddle icon"><span class="bubble"></span><span class="glyph"></span></div>PADDLE</div>
  <div class="feature" style="left:468px;top:1020px;padding-top:0"><div class="feature-icon" role="img" aria-label="Shuttle bus icon" style="margin-top:4px;height:58px"><span class="bubble"></span><span class="glyph" style="height:44px"></span></div>ROUND TRIP<br>SHUTTLE SERVICE</div>
  <div class="feature" style="left:120px;top:1130px"><div class="feature-icon" role="img" aria-label="Safety training icon"><span class="bubble"></span><span class="glyph"></span></div>SAFETY<br>TRAINING</div>
  <div class="feature" style="left:282px;top:1130px"><div class="feature-icon" role="img" aria-label="Staff assistance icon"><span class="bubble"></span><span class="glyph"></span></div>STAFF<br>ASSISTANCE</div>
  <div class="feature" style="left:468px;top:1140px"><div class="feature-icon" role="img" aria-label="Parking icon"><span class="bubble"></span><span class="glyph"></span></div>PARKING</div>

  <div class="includes-photo" role="img" aria-label="Smiling child floating in a red river tube"></div>
</section>

<section>
  <div class="group-band" role="img" aria-label="Group of friends floating in tubes on the river"></div>
  <h2 class="group-title">GROUP OF 10 OR MORE?</h2>
  <p class="group-note">*does not include taxes or fees</p>
  <div class="btn btn-orange" style="left:856px;top:1425px;width:185px;height:40px">Contact Us<span class="dot"><svg viewBox="0 0 10 10"><path d="M3 1l4 4-4 4" fill="none" stroke="#F0912C" stroke-width="2"/></svg></span></div>
</section>

<section class="about">
  <div class="about-bg"></div>
  <svg class="abs" style="left:70px;top:1625px" width="500" height="420" viewBox="0 0 500 420">
    <path d="M14 370 C0 240 40 60 250 5 C420 -15 500 160 490 310" fill="none" stroke="var(--orange)" stroke-width="3"/>
    <circle cx="22" cy="360" r="14" fill="none" stroke="var(--orange)" stroke-width="3"/>
    <circle cx="46" cy="382" r="17" fill="none" stroke="var(--orange)" stroke-width="3"/>
    <circle cx="420" cy="360" r="16" fill="none" stroke="var(--orange)" stroke-width="3"/>
    <circle cx="446" cy="382" r="11" fill="none" stroke="var(--orange)" stroke-width="3"/>
  </svg>
  <div class="about-photo" role="img" aria-label="Two friends relaxing on inflatable rings in clear water"></div>
  <h2 class="about-title">ABOUT US</h2>
  <p class="about-lead">Float the North Saskatchewan through downtown Edmonton Edmonton's Best Summer Activity</p>
  <p class="about-copy" style="top:1767px">We provide the lifejacket, paddle, river tube and shuttle service. You just have to show up. Brisbeck Current Glide was launched to provide people in the Edmonton area a favorite summer activity. Nothing is better on a hot summer day, than spending it on the river and seeing Edmonton from a new perspective.</p>
  <p class="about-copy" style="top:1897px">Our home base and meeting spot is at Alder Quay Landing (<a>Map Link</a>), by the Glasshouse Pavilion. This is where you will check in, and board the shuttle.</p>
  <div class="btn btn-sky" style="left:600px;top:1993px;width:160px;height:36px;font-size:14px">Learn More<span class="dot"><svg viewBox="0 0 10 10"><path d="M3 1l4 4-4 4" fill="none" stroke="#52c4e7" stroke-width="2"/></svg></span></div>
  <div class="btn btn-navy" style="left:771px;top:1993px;width:152px;height:36px;font-size:14px">Book Now<span class="dot"><svg viewBox="0 0 10 10"><path d="M3 1l4 4-4 4" fill="none" stroke="#0b2d5e" stroke-width="2"/></svg></span></div>
</section>

<section class="faq">
  <div class="faq-band"></div>
  <h2 class="faq-title">Frequently Asked Questions</h2>
  <div class="faq-item" style="left:174px;top:2274px"><span class="toggle"><svg width="14" height="9" viewBox="0 0 14 9"><path d="M2 2l5 5 5-5" fill="none" stroke="#fff" stroke-width="2"/></svg></span><span class="q">How do I reserve my float?</span></div>
  <div class="faq-item open" style="left:174px;top:2338px"><span class="toggle"><svg width="14" height="9" viewBox="0 0 14 9"><path d="M2 7l5-5 5 5" fill="none" stroke="#fff" stroke-width="2"/></svg></span><span class="q">What safety information should I know?</span></div>
  <div class="faq-answer">Children 12 years and younger should be accompanied by an adult at all times on the river. Life jackets and paddles are provided and are<u>LEARN MORE</u></div>
  <div class="faq-item" style="left:602px;top:2274px"><span class="toggle"><svg width="14" height="9" viewBox="0 0 14 9"><path d="M2 2l5 5 5-5" fill="none" stroke="#fff" stroke-width="2"/></svg></span><span class="q">How do I reserve my float?</span></div>
  <div class="faq-item" style="left:602px;top:2338px"><span class="toggle"><svg width="14" height="9" viewBox="0 0 14 9"><path d="M2 2l5 5 5-5" fill="none" stroke="#fff" stroke-width="2"/></svg></span><span class="q">How do I reserve my float?</span></div>
  <div class="faq-item" style="left:602px;top:2402px"><span class="toggle"><svg width="14" height="9" viewBox="0 0 14 9"><path d="M2 2l5 5 5-5" fill="none" stroke="#fff" stroke-width="2"/></svg></span><span class="q">How do I reserve my float?</span></div>
  <div class="faq-item" style="left:602px;top:2466px"><span class="toggle"><svg width="14" height="9" viewBox="0 0 14 9"><path d="M2 2l5 5 5-5" fill="none" stroke="#fff" stroke-width="2"/></svg></span><span class="q">How do I reserve my float?</span></div>
  <div class="btn btn-navy" style="left:523px;top:2571px;width:154px;height:36px;font-size:14px;letter-spacing:1px">View More<span class="dot"><svg viewBox="0 0 10 10"><path d="M3 1l4 4-4 4" fill="none" stroke="#0b2d5e" stroke-width="2"/></svg></span></div>
</section>

<section class="contact">
  <div class="map" role="img" aria-label="Street map of the river valley around the meeting point"></div>
  <div class="contact-card">
    <h2>CONTACT US</h2>
    <p class="tag">We'd love to hear from you!</p>
    <div class="contact-line"><span class="ring"><svg viewBox="0 0 10 10"><path d="M2 1l2 0 1 2-1 1c1 2 2 3 3 3l1-1 2 1 0 2c-5 0-8-3-8-8z" fill="#fff"/></svg></span>780 555 0148</div>
    <div class="contact-line"><span class="ring"><svg viewBox="0 0 10 10"><rect x="1" y="2" width="8" height="6" fill="none" stroke="#fff"/><path d="M1 2l4 3 4-3" fill="none" stroke="#fff"/></svg></span>hello@brisbeckglide.example</div>
    <div class="socials"><span></span><span></span><span></span></div>
    <p class="visit">Come visit us on float days at<br>Alder Quay Landing</p>
  </div>
</section>

<footer>
  <svg class="abs" style="left:0;top:3310px" width="1200" height="521" viewBox="0 0 1200 521">
    <path d="M0 40 C40 20 80 50 130 35 C180 20 210 5 260 28 C300 45 330 20 380 30 C420 38 450 8 500 18 C560 30 600 50 650 30 C700 10 740 40 790 35 C840 30 870 5 920 20 C960 32 1000 45 1050 28 C1100 12 1150 30 1200 22 L1200 521 L0 521 Z" fill="var(--navy)"/>
    <path d="M0 430 C80 410 160 440 240 425 C330 408 420 440 520 428 C620 415 720 440 820 425 C920 410 1020 438 1200 420 L1200 521 L0 521 Z" fill="#08234b"/>
  </svg>
  <div class="footer-brand"><div class="brand-mark"></div><div class="brand-name">Brisbeck Current Glide</div></div>
  <div class="socials abs" style="left:216px;top:3646px;color:#fff"><span></span><span></span><span></span></div>
  <h3 class="footer-col-title" style="left:526px;top:3478px">Our Links</h3>
  <span class="footer-link" style="left:526px;top:3535px;color:var(--faq)">HOME</span>
  <span class="footer-link" style="top:3570px">PRICING</span>
  <span class="footer-link" style="top:3604px">ABOUT</span>
  <span class="footer-link" style="top:3639px">FAQ</span>
  <span class="footer-link" style="top:3673px">CONTACT</span>
  <h3 class="footer-col-title" style="left:742px;top:3478px">Brisbeck Current Glide</h3>
  <span class="abs" style="left:742px;top:3524px;font-size:19px;font-weight:600;color:var(--faq);letter-spacing:.5px">CONNECT</span>
  <div class="contact-line abs" style="left:744px;top:3548px;color:#fff;font-size:15px"><span class="ring"><svg viewBox="0 0 10 10"><path d="M2 1l2 0 1 2-1 1c1 2 2 3 3 3l1-1 2 1 0 2c-5 0-8-3-8-8z" fill="#fff"/></svg></span>780 555 0148</div>
  <div class="contact-line abs" style="left:744px;top:3579px;color:#fff;font-size:15px"><span class="ring"><svg viewBox="0 0 10 10"><rect x="1" y="2" width="8" height="6" fill="none" stroke="#fff"/><path d="M1 2l4 3 4-3" fill="none" stroke="#fff"/></svg></span>hello@brisbeckglide.example</div>
  <div class="btn btn-sky" style="left:745px;top:3652px;width:160px;height:37px">Book Now<span class="dot"><svg viewBox="0 0 10 10"><path d="M3 1l4 4-4 4" fill="none" stroke="#52c4e7" stroke-width="2"/></svg></span></div>
  <p class="copyright">© Copyright 2022 Brisbeck Current Glide. All rights reserved.</p>
</footer>

</body>
</html>
```